I need a business card/logo designed that obviously describes my business. We are a residential appraisal and home inspection company in Springfield, MO. We offer residential appraisals, home inspection, pest inspection and radon gas measurement. We have been in business for 18 years and hold state certified residential appraisal licenses and DRUMI certified home inspection licenses. I have a logo that I really like and will attach, but would be open to new suggestions. I like more modern designs than traditional and would like a two sided card with our services, licenses and qualifications on the back.

```html
<!DOCTYPE html>
<html lang="en">
<head>
<meta charset="utf-8">
<title>Larkvale Dwelling Review – Business Card</title>
<link href="https://fonts.googleapis.com/css2?family=Source+Sans+3:ital,wght@0,400;0,600;1,400&display=swap" rel="stylesheet">
<style>
  :root {
    --backdrop: #2d2d2d;
    --paper: #ffffff;
    --tan-light: #ab8c5c;
    --tan-dark: #96784a;
    --orange: #f7a623;
    --orange-deep: #f3951b;
    --text-light: #fbf6ee;
    --text-tan: #9b7d4d;
  }
  * { margin: 0; padding: 0; box-sizing: border-box; }
  html, body { width: 1200px; height: 659px; overflow: hidden; }
  body {
    background: var(--backdrop);
    font-family: "Source Sans 3", "Myriad Pro", sans-serif;
    position: relative;
  }
  .card {
    position: absolute;
    top: 186px;
    width: 500px;
    height: 286px;
    overflow: hidden;
  }
  .card--front { left: 70px; background: var(--paper); }
  .card--back {
    left: 630px;
    background: linear-gradient(135deg, var(--orange-deep), var(--orange) 55%, var(--orange-deep));
  }

  /* front */
  .front__panel {
    position: absolute;
    top: 0; right: 0;
    width: 228px; height: 100%;
    background: linear-gradient(200deg, var(--tan-light), var(--tan-dark));
  }
  .front__divider { position: absolute; top: 0; left: 262px; }
  .brand {
    position: absolute;
    left: 34px; top: 128px;
    display: flex; align-items: center; gap: 10px;
  }
  .brand__mark { width: 14px; height: 14px; background: var(--orange); }
  .brand__name {
    font-weight: 600;
    font-size: 17px;
    color: var(--text-tan);
    letter-spacing: 0.3px;
  }
  .contact {
    position: absolute;
    left: 296px; top: 46px;
    color: var(--text-light);
    font-size: 11.5px;
    line-height: 1.45;
  }
  .contact__name { color: var(--orange); font-size: 17px; font-weight: 600; line-height: 1.1; }
  .contact__role { margin-bottom: 14px; }
  .contact__address { margin-bottom: 10px; }
  .contact__row { display: flex; align-items: center; gap: 7px; }
  .contact__icon { width: 11px; height: 11px; flex: none; }

  /* back */
  .back__brand {
    position: absolute;
    left: 0; right: 0; top: 56px;
    text-align: center;
    color: var(--paper);
    font-weight: 600;
    font-size: 24px;
  }
  .back__rule {
    position: absolute;
    left: 40px; right: 40px; top: 112px;
    height: 1px;
    background: rgba(255, 255, 255, 0.55);
  }
  .back__columns {
    position: absolute;
    left: 40px; right: 40px; top: 132px;
    display: flex;
    gap: 30px;
    color: var(--paper);
  }
  .back__column--services { width: 170px; flex: none; }
  .back__column--credentials { flex: 1; }
  .back__heading {
    font-size: 12.5px;
    font-weight: 600;
    margin-bottom: 6px;
    text-transform: uppercase;
    letter-spacing: 0.6px;
  }
  .back__list {
    list-style: none;
    font-size: 12px;
    font-style: italic;
    line-height: 1.55;
  }
  .back__list li::before { content: "• "; font-style: normal; }
</style>
</head>
<body>
  <section class="card card--front" aria-label="Business card front">
    <div class="front__panel"></div>
    <svg class="front__divider" width="14" height="286" viewBox="0 0 14 286" aria-hidden="true">
      <polyline points="10,0 10,132 3,138 10,144 10,286" fill="none" stroke="var(--orange)" stroke-width="3"/>
    </svg>
    <div class="brand">
      <span class="brand__mark"></span>
      <span class="brand__name">Larkvale Dwelling Review</span>
    </div>
    <div class="contact">
      <p class="contact__name">Mara Quillon</p>
      <p class="contact__role">CEO/Founder</p>
      <p class="contact__address">412 Fenwick Row<br>Harrowgate, Ohio 40718</p>
      <p class="contact__row">
        <svg class="contact__icon" viewBox="0 0 12 12" aria-hidden="true"><path d="M2 1h3l1 3-2 1a7 7 0 0 0 3 3l1-2 3 1v3c-6 0-10-4-10-9z" fill="var(--orange)"/></svg>
        555 204 7731
      </p>
      <p class="contact__row">
        <svg class="contact__icon" viewBox="0 0 12 12" aria-hidden="true"><rect x="1" y="3" width="10" height="7" rx="1" fill="var(--orange)"/><rect x="3" y="1" width="6" height="3" fill="var(--orange)"/></svg>
        555 318 6642
      </p>
      <p class="contact__row">
        <svg class="contact__icon" viewBox="0 0 12 12" aria-hidden="true"><rect x="1" y="2" width="10" height="8" fill="var(--orange)"/><polyline points="1,2 6,7 11,2" fill="none" stroke="var(--tan-dark)" stroke-width="1"/></svg>
        mara@larkvalereview.com
      </p>
      <p class="contact__row">
        <svg class="contact__icon" viewBox="0 0 12 12" aria-hidden="true"><circle cx="6" cy="6" r="5" fill="var(--orange)"/></svg>
        www.larkvalereview.com
      </p>
    </div>
  </section>

  <section class="card card--back" aria-label="Business card back">
    <p class="back__brand">Larkvale Dwelling Review</p>
    <div class="back__rule"></div>
    <div class="back__columns">
      <div class="back__column back__column--services">
        <p class="back__heading">Services</p>
        <ul class="back__list">
          <li>Residential appraisal</li>
          <li>Home inspection</li>
          <li>Pest inspection</li>
          <li>Radon gas measurement</li>
        </ul>
      </div>
      <div class="back__column back__column--credentials">
        <p class="back__heading">Licenses &amp; qualifications</p>
        <ul class="back__list">
          <li>18 years in business</li>
          <li>State certified residential appraiser</li>
          <li>DRUMI certified home inspector</li>
        </ul>
      </div>
    </div>
  </section>
</body>
</html>
```